Slide Master for Harrowfield Engines - A Systematic Hedge Fund

We are looking for someone to produce a theme and slide master for us for our investor presentations. I have uploaded a few examples of templates that we would like to have included:
Main Title
Section Title
Slides with just bullet points
Different image/table configurations with bullet points and foot notes
Biographies of different lengths
A disclaimer (no one will read this but it should still look nice and needs to be in the presentations)
I have also uploaded the company logo, business card and colour definitions. Currently we have a blue colour scheme defined, but it would be nice to get a complementary set of colours so that when we have charts with more elements we can just draw from those.
The most important thing is that the slide master must be of general use to us. We arn't looking to have a specific presentation designed for us, but a theme/style that we can apply ourselves to any presentation we need to give in the future. It should have clearly defined guidelines for where content should go (and if this is different with and without footnotes for example). We would also like it to have a similar feel to the logo/business cards, so matt colours, high contrast, but not busy.
I'm excited to see the results!

```html
<!DOCTYPE html>
<html lang="en">
<head>
<meta charset="utf-8">
<title>Harrowfield Engines – Slide Master Overview</title>
<link href="https://fonts.googleapis.com/css2?family=Roboto:wght@400;500;700&display=swap" rel="stylesheet">
<style>
:root{
  --board:#e8e7e9;
  --paper:#ffffff;
  --navy:#0c3a6b;
  --navy-deep:#06203f;
  --blue:#3b7fc4;
  --sky:#a9c8e8;
  --mist:#dde3ea;
  --ink:#222a33;
  --grey:#8a919a;
  --placeholder:#dcdee2;
}
*{margin:0;padding:0;box-sizing:border-box}
html,body{width:1000px;height:1200px;overflow:hidden;background:var(--board)}
body{position:relative;font-family:'Roboto',Arial,sans-serif;color:var(--ink)}
.slide{position:absolute;width:485px;height:273px;background:var(--paper);transform-origin:0 0;transform:scale(.5714);overflow:hidden;box-shadow:0 2px 6px rgba(0,0,0,.18)}
.slide>*{position:absolute}
.c1{left:74px}.c2{left:361px}.c3{left:648px}
.r1{top:41px}.r2{top:202px}.r3{top:363px}.r4{top:523px}.r5{top:684px}.r6{top:845px}.r7{top:1005px}

/* chrome */
.rule{left:33px;right:33px;top:249px;height:.6px;background:var(--sky)}
.dots{right:33px;top:246px;width:20px;border-top:1.4px dotted var(--navy)}
.brand{left:33px;top:252px;font-size:4.6px;font-weight:700;color:var(--navy);letter-spacing:.2px}
.meta{right:33px;top:258px;font-size:2.8px;color:var(--grey);word-spacing:6px}
.note{left:33px;top:233px;font-size:2.7px;line-height:1.5;color:var(--grey)}

/* type */
.title{left:33px;top:23px;font-size:15px;font-weight:700;color:var(--navy)}
.sub{left:33px;top:44px;font-size:8px;color:var(--blue)}
.p{font-size:5.4px;line-height:1.38;color:var(--ink)}
.small{font-size:4.4px;line-height:1.38;color:var(--ink)}
.hd{font-size:4.6px;font-weight:700;color:var(--ink)}
ul.list{list-style:none}
ul.list li{position:relative;padding-left:8px;margin-bottom:2px}
ul.list li::before{content:"";position:absolute;left:1px;top:2px;width:2px;height:2px;border-radius:50%;background:var(--ink)}
ul.tiny li{padding-left:6px;margin-bottom:1.5px}
ul.tiny li::before{top:1.6px;width:1.6px;height:1.6px}

/* cover */
.cover .backdrop{left:0;top:0;width:100%;height:100%}
.cover.dark .backdrop{background:radial-gradient(ellipse at 50% 30%,#1f5c9a 0%,#0a2a52 45%,#04101f 100%)}
.cover.light .backdrop{background:radial-gradient(ellipse at 55% 40%,#5f9ad8 0%,#3f7fc4 45%,#2d67a8 100%)}
.cover .wordmark{left:0;right:0;top:88px;text-align:center;font-size:17px;font-weight:700;letter-spacing:.6px}
.cover.dark .wordmark{color:#fff}
.cover.light .wordmark{color:var(--navy)}
.cover .ptitle{left:0;right:0;top:166px;text-align:center;font-size:18px;font-weight:700;color:#fff}
.cover .psub{left:0;right:0;top:193px;text-align:center;font-size:8px;color:#e4eef9}

/* blocks */
.photo{background:linear-gradient(135deg,#d9d3c6 0%,#b8a68f 40%,#6c6f74 75%,#3e4a58 100%)}
.tech{background:radial-gradient(circle at 64% 52%,#d9f4ff 0%,#3aa9e8 6%,#0e4c86 28%,#06203f 70%)}
.placeholder{background:var(--placeholder)}
.bar-head{background:var(--navy);color:#fff;font-size:4.8px;font-weight:700;padding:3px 4px}
.key{background:var(--navy);color:#fff}
.key .kh{position:absolute;left:5px;right:5px;top:7px;background:var(--blue);font-size:4.6px;font-weight:700;padding:3px 4px}
.key ul{position:absolute;left:8px;right:6px;top:26px;color:#fff}
.key ul li::before{background:#fff}
.underhead{font-size:5px;font-weight:700;color:var(--ink);border-bottom:.8px solid var(--blue);padding-bottom:1.5px}
.band{background:var(--navy);color:#fff;font-size:6.6px;padding:7px 10px}
table.grid{border-collapse:collapse;font-size:4px;color:var(--ink)}
table.grid td,table.grid th{border:.6px solid var(--sky);padding:0 2px;text-align:left;height:14.6px}
table.grid th{font-size:6.4px;font-weight:700;height:14px;border-bottom:1px solid var(--navy)}
table.grid tr:nth-child(even) td{background:#f2f6fb}
</style>
</head>
<body>

<!-- Row 1 -->
<section class="slide cover dark c1 r1">
  <div class="backdrop" role="img" aria-label="Dark navy backdrop with a glowing network of connected points"></div>
  <div class="wordmark">HARROWFIELD ENGINES</div>
  <div class="ptitle">Presentation title</div>
  <div class="psub">subtitle</div>
</section>

<section class="slide cover light c2 r1">
  <div class="backdrop" role="img" aria-label="Bright blue backdrop with a faint network of connected points"></div>
  <div class="wordmark">HARROWFIELD ENGINES</div>
  <div class="ptitle">Presentation title</div>
  <div class="psub">subtitle</div>
</section>

<section class="slide c3 r1">
  <div style="left:0;right:0;top:42px;text-align:center;font-size:8px;font-weight:700;color:var(--navy)">Disclaimer</div>
  <p class="small" style="left:72px;width:341px;top:106px;text-align:center">Lorem ipsum dolor sit amet, consectetur adipiscing elit. Vestibulum lacinia eros eu pharetra mollis. Nullam vulputate purus mi, sed maximus est sodales mollis. Mauris nec vulputate eros. Cras lectus lacus, lacinia eu dapibus ac, tincidunt eu nisi. Suspendisse in volutpat risus. Nunc pharetra porttitor lorem. Vivamus at lectus sit amet lacus dictum tincidunt at vel magna. Donec blandit nulla ac erat condimentum, fringilla feugiat ex porttitor. Proin est odio, suscipit vitae magna at, bibendum tincidunt mi. Aenean facilisis pharetra lacus sed tempus. Nam finibus eu diam eu consectetur. Donec blandit nulla ac erat condimentum, fringilla feugiat ex porttitor. Proin est odio, suscipit vitae magna at, bibendum tincidunt mi. Aenean facilisis pharetra lacus sed tempus. Nam finibus eu diam eu consectetur.</p>
  <div class="rule"></div><div class="dots"></div><div class="brand">HARROWFIELD ENGINES</div>
</section>

<!-- Row 2 -->
<section class="slide c1 r2">
  <div style="left:33px;top:42px;font-size:7.6px;font-weight:700;color:var(--navy)">Disclaimer</div>
  <p class="small" style="left:33px;width:126px;top:98px">Lorem ipsum dolor sit amet, consectetur adipiscing elit. Vestibulum lacinia eros eu pharetra mollis. Nullam vulputate purus mi, sed maximus est sodales mollis. Mauris nec vulputate eros. Cras lectus lacus, lacinia eu dapibus ac, tincidunt eu nisi. Suspendisse in volutpat risus. Nunc pharetra porttitor lorem. Vivamus at lectus sit amet lacus dictum tincidunt at vel magna. Donec blandit nulla ac erat condimentum, fringilla feugiat ex porttitor.</p>
  <p class="small" style="left:180px;width:126px;top:98px">Lorem ipsum dolor sit amet, consectetur adipiscing elit. Vestibulum lacinia eros eu pharetra mollis. Nullam vulputate purus mi, sed maximus est sodales mollis. Mauris nec vulputate eros. Cras lectus lacus, lacinia eu dapibus ac, tincidunt eu nisi. Suspendisse in volutpat risus. Nunc pharetra porttitor lorem. Vivamus at lectus sit amet lacus dictum tincidunt at vel magna. Donec blandit nulla ac erat condimentum, fringilla feugiat ex porttitor.</p>
  <p class="small" style="left:327px;width:126px;top:98px">Lorem ipsum dolor sit amet, consectetur adipiscing elit. Vestibulum lacinia eros eu pharetra mollis. Nullam vulputate purus mi, sed maximus est sodales mollis. Mauris nec vulputate eros. Cras lectus lacus, lacinia eu dapibus ac, tincidunt eu nisi. Suspendisse in volutpat risus. Nunc pharetra porttitor lorem. Vivamus at lectus sit amet lacus dictum tincidunt at vel magna. Donec blandit nulla ac erat condimentum, fringilla feugiat ex porttitor.</p>
  <div class="rule"></div><div class="dots"></div><div class="brand">HARROWFIELD ENGINES</div>
</section>

<section class="slide c2 r2">
  <h2 class="title">Slide title</h2><div class="sub">Sub title</div>
  <ul class="list p" style="left:33px;top:71px;font-size:5px">
    <li>Bullet level 1</li>
    <li style="margin-left:8px">Bullet level 2</li>
    <li style="margin-left:18px">Bullet level 3</li>
    <li style="margin-left:28px">Bullet level 4</li>
    <li style="margin-left:38px">Bullet level 5</li>
  </ul>
  <div class="note">Footnote here<br>Source here</div>
  <div class="rule"></div><div class="dots"></div><div class="brand">HARROWFIELD ENGINES</div>
  <div class="meta">Date | 09-06-2021 Page | 6</div>
</section>

<section class="slide c3 r2">
  <h2 class="title">Slide title</h2><div class="sub">Sub title</div>
  <p class="p" style="left:33px;width:172px;top:79px">Lorem ipsum dolor sit amet, consectetur adipiscing elit. Vestibulum lacinia eros eu pharetra mollis. Nullam vulputate purus mi, sed maximus est sodales mollis. Mauris nec vulputate eros. Cras lectus lacus, lacinia eu dapibus ac, tincidunt eu nisi. Suspendisse in volutpat risus. Nunc pharetra porttitor lorem. Vivamus at lectus sit amet lacus dictum tincidunt at vel magna. Donec blandit nulla ac erat condimentum, fringilla feugiat ex porttitor. Proin est odio, suscipit vitae magna at, bibendum tincidunt mi. Aenean facilisis pharetra lacus sed tempus. Nam finibus eu diam eu consectetur.</p>
  <svg style="left:225px;top:70px" width="230" height="145" viewBox="0 0 230 145" font-family="Roboto, sans-serif">
    <text x="117" y="12" font-size="6" fill="#555" text-anchor="middle">Chart Title</text>
    <g stroke="#e2e5e9" stroke-width=".5">
      <line x1="22" y1="22" x2="225" y2="22"/><line x1="22" y1="37.7" x2="225" y2="37.7"/>
      <line x1="22" y1="53.3" x2="225" y2="53.3"/><line x1="22" y1="69" x2="225" y2="69"/>
      <line x1="22" y1="84.7" x2="225" y2="84.7"/><line x1="22" y1="100.3" x2="225" y2="100.3"/>
      <line x1="22" y1="116" x2="225" y2="116"/>
    </g>
    <g font-size="4.2" fill="#666" text-anchor="end">
      <text x="14" y="24">6</text><text x="14" y="39.5">5</text><text x="14" y="55">4</text><text x="14" y="71">3</text>
      <text x="14" y="86.5">2</text><text x="14" y="102">1</text><text x="14" y="118">0</text>
    </g>
    <g>
      <rect x="38" y="48.6" width="6" height="67.4" fill="#0c3a6b"/><rect x="45" y="78.4" width="6" height="37.6" fill="#3b7fc4"/><rect x="52" y="84.7" width="6" height="31.3" fill="#a9c8e8"/>
      <rect x="88" y="76.8" width="6" height="39.2" fill="#0c3a6b"/><rect x="95" y="47" width="6" height="69" fill="#3b7fc4"/><rect x="102" y="84.7" width="6" height="31.3" fill="#a9c8e8"/>
      <rect x="138" y="61.2" width="6" height="54.8" fill="#0c3a6b"/><rect x="145" y="87.8" width="6" height="28.2" fill="#3b7fc4"/><rect x="152" y="69" width="6" height="47" fill="#a9c8e8"/>
      <rect x="188" y="45.5" width="6" height="70.5" fill="#0c3a6b"/><rect x="195" y="72.1" width="6" height="43.9" fill="#3b7fc4"/><rect x="202" y="37.7" width="6" height="78.3" fill="#a9c8e8"/>
    </g>
    <g font-size="4.4" fill="#666" text-anchor="middle">
      <text x="48" y="126">Category 1</text><text x="98" y="126">Category 2</text><text x="148" y="126">Category 3</text><text x="198" y="126">Category 4</text>
    </g>
    <g font-size="4.2" fill="#666">
      <rect x="72" y="136" width="3" height="3" fill="#0c3a6b"/><text x="77" y="139">Series 1</text>
      <rect x="102" y="136" width="3" height="3" fill="#3b7fc4"/><text x="107" y="139">Series 2</text>
      <rect x="132" y="136" width="3" height="3" fill="#a9c8e8"/><text x="137" y="139">Series 3</text>
    </g>
  </svg>
  <div class="note">Footnote here<br>Source here</div>
  <div class="rule"></div><div class="dots"></div><div class="brand">HARROWFIELD ENGINES</div>
  <div class="meta">Date | 09-06-2021 Page | 7</div>
</section>

<!-- Row 3 -->
<section class="slide c1 r3">
  <h2 class="title">Slide title</h2><div class="sub">Sub title</div>
  <ul class="list p" style="left:33px;top:70px;width:205px">
    <li>Lorem ipsum dolor sit amet, consectetur adipiscing elit. Vestibulum lacinia eros eu pharetra mollis.</li>
    <li>Nullam vulputate purus mi, sed maximus est sodales mollis. Mauris nec vulputate eros.</li>
    <li>Cras lectus lacus, lacinia eu dapibus ac, tincidunt eu nisi. Suspendisse in volutpat risus.</li>
    <li>Nunc pharetra porttitor lorem. Vivamus at lectus sit amet lacus dictum tincidunt at vel magna.</li>
    <li>Donec blandit nulla ac erat condimentum, fringilla feugiat ex porttitor.</li>
    <li>Proin est odio, suscipit vitae magna at, bibendum tincidunt mi. Aenean facilisis pharetra lacus sed tempus.</li>
    <li>Nam finibus eu diam eu consectetur.</li>
  </ul>
  <ul class="list p" style="left:250px;top:70px;width:205px">
    <li>Lorem ipsum dolor sit amet, consectetur adipiscing elit. Vestibulum lacinia eros eu pharetra mollis.</li>
    <li>Nullam vulputate purus mi, sed maximus est sodales mollis. Mauris nec vulputate eros.</li>
    <li>Cras lectus lacus, lacinia eu dapibus ac, tincidunt eu nisi. Suspendisse in volutpat risus.</li>
    <li>Nunc pharetra porttitor lorem. Vivamus at lectus sit amet lacus dictum tincidunt at vel magna.</li>
    <li>Donec blandit nulla ac erat condimentum, fringilla feugiat ex porttitor.</li>
    <li>Proin est odio, suscipit vitae magna at, bibendum tincidunt mi. Aenean facilisis pharetra lacus sed tempus.</li>
    <li>Nam finibus eu diam eu consectetur.</li>
  </ul>
  <div class="note">Footnote here<br>Source here</div>
  <div class="rule"></div><div class="dots"></div><div class="brand">HARROWFIELD ENGINES</div>
  <div class="meta">Date | 09-06-2021 Page | 8</div>
</section>

<section class="slide c2 r3">
  <h2 class="title">Slide title</h2><div class="sub">Sub title</div>
  <div class="bar-head" style="left:33px;top:88px;width:60px">Heading</div>
  <ul class="list tiny small" style="left:98px;top:89px;width:76px"><li>Lorem ipsum dolor sit amet, consectetur adipiscing elit. Vestibulum lacinia eros eu pharetra mollis.</li></ul>
  <div class="bar-head" style="left:33px;top:137px;width:60px">Heading</div>
  <ul class="list tiny small" style="left:98px;top:138px;width:76px"><li>Lorem ipsum dolor sit amet, consectetur adipiscing elit. Vestibulum lacinia eros eu pharetra mollis.</li></ul>
  <div class="bar-head" style="left:33px;top:187px;width:60px">Heading</div>
  <ul class="list tiny small" style="left:98px;top:188px;width:76px"><li>Lorem ipsum dolor sit amet, consectetur adipiscing elit. Vestibulum lacinia eros eu pharetra mollis.</li></ul>
  <div class="bar-head" style="left:259px;top:88px;width:60px">Heading</div>
  <ul class="list tiny small" style="left:331px;top:89px;width:80px"><li>Lorem ipsum dolor sit amet, consectetur adipiscing elit. Vestibulum lacinia eros eu pharetra mollis.</li></ul>
  <div class="bar-head" style="left:259px;top:137px;width:60px">Heading</div>
  <ul class="list tiny small" style="left:331px;top:138px;width:80px"><li>Lorem ipsum dolor sit amet, consectetur adipiscing elit. Vestibulum lacinia eros eu pharetra mollis.</li></ul>
  <div class="bar-head" style="left:259px;top:187px;width:60px">Heading</div>
  <ul class="list tiny small" style="left:331px;top:188px;width:80px"><li>Lorem ipsum dolor sit amet, consectetur adipiscing elit. Vestibulum lacinia eros eu pharetra mollis.</li></ul>
  <div class="note">Footnote here<br>Source here</div>
  <div class="rule"></div><div class="dots"></div><div class="brand">HARROWFIELD ENGINES</div>
  <div class="meta">Date | 09-06-2021 Page | 9</div>
</section>

<section class="slide c3 r3">
  <h2 class="title">Slide title</h2><div class="sub">subtitle</div>
  <ul class="list p" style="left:33px;top:65px;width:250px">
    <li>Lorem ipsum dolor sit amet, consectetur adipiscing elit. Vestibulum lacinia eros eu pharetra mollis.</li>
    <li>Nullam vulputate purus mi, sed maximus est sodales mollis. Mauris nec vulputate eros.</li>
    <li>Cras lectus lacus, lacinia eu dapibus ac, tincidunt eu nisi. Suspendisse in volutpat risus.</li>
    <li>Nunc pharetra porttitor lorem. Vivamus at lectus sit amet lacus dictum tincidunt at vel magna.</li>
    <li>Donec blandit nulla ac erat condimentum, fringilla feugiat ex porttitor.</li>
    <li>Proin est odio, suscipit vitae magna at, bibendum tincidunt mi. Aenean facilisis pharetra lacus sed tempus.</li>
    <li>Nam finibus eu diam eu consectetur.</li>
  </ul>
  <div class="key" style="left:328px;top:58px;width:124px;height:168px">
    <div class="kh">Key takeaway</div>
    <ul class="list tiny small">
      <li>Lorem ipsum dolor sit amet, consectetur adipiscing elit. Vestibulum lacinia eros eu pharetra mollis.</li>
      <li>Nullam vulputate purus mi, sed maximus est sodales mollis. Mauris nec vulputate eros.</li>
      <li>Cras lectus lacus, lacinia eu dapibus ac, tincidunt eu nisi.</li>
      <li>Suspendisse in volutpat risus. Nunc pharetra porttitor lorem.</li>
      <li>Suspendisse in volutpat risus. Nunc pharetra porttitor lorem.</li>
    </ul>
  </div>
  <div class="note">Footnote here<br>Source</div>
  <div class="rule"></div><div class="dots"></div><div class="brand">HARROWFIELD ENGINES</div>
  <div class="meta">Date | 09-06-2021 Page | 10</div>
</section>

<!-- Row 4 -->
<section class="slide c1 r4">
  <h2 class="title">Slide title</h2><div class="sub">Sub title</div>
  <div class="photo" style="left:33px;top:74px;width:98px;height:66px" role="img" aria-label="Photo of a team meeting around a whiteboard"></div>
  <div class="photo" style="left:140px;top:74px;width:98px;height:66px" role="img" aria-label="Photo of a team meeting around a whiteboard"></div>
  <div class="photo" style="left:247px;top:74px;width:98px;height:66px" role="img" aria-label="Photo of a team meeting around a whiteboard"></div>
  <div class="photo" style="left:354px;top:74px;width:98px;height:66px" role="img" aria-label="Photo of a team meeting around a whiteboard"></div>
  <div style="left:33px;top:146px;width:98px"><div class="hd">Header</div><p class="small">Lorem ipsum dolor sit amet, consectetur adipiscing elit. Vestibulum lacinia eros eu pharetra mollis.</p></div>
  <div style="left:140px;top:146px;width:98px"><div class="hd">Header</div><p class="small">Lorem ipsum dolor sit amet, consectetur adipiscing elit. Vestibulum lacinia eros eu pharetra mollis.</p></div>
  <div style="left:247px;top:146px;width:98px"><div class="hd">Header</div><p class="small">Lorem ipsum dolor sit amet, consectetur adipiscing elit. Vestibulum lacinia eros eu pharetra mollis.</p></div>
  <div style="left:354px;top:146px;width:98px"><div class="hd">Header</div><p class="small">Lorem ipsum dolor sit amet, consectetur adipiscing elit. Vestibulum lacinia eros eu pharetra mollis.</p></div>
  <div class="note">Footnote here<br>Source here</div>
  <div class="rule"></div><div class="dots"></div><div class="brand">HARROWFIELD ENGINES</div>
  <div class="meta">Date | 09-06-2021 Page | 11</div>
</section>

<section class="slide c2 r4">
  <h2 class="title">Slide title</h2><div class="sub">Sub title</div>
  <div class="photo" style="left:33px;top:71px;width:98px;height:66px" role="img" aria-label="Photo of a team meeting around a whiteboard"></div>
  <div style="left:140px;top:72px;width:98px"><div class="hd">Header</div><p class="small">Lorem ipsum dolor sit amet, consectetur adipiscing elit. Vestibulum lacinia eros eu pharetra mollis.</p></div>
  <div class="photo" style="left:248px;top:71px;width:98px;height:66px" role="img" aria-label="Photo of a team meeting around a whiteboard"></div>
  <div style="left:355px;top:72px;width:98px"><div class="hd">Heading</div><p class="small">Lorem ipsum dolor sit amet, consectetur adipiscing elit. Vestibulum lacinia eros eu pharetra mollis.</p></div>
  <div class="photo" style="left:33px;top:152px;width:98px;height:66px" role="img" aria-label="Photo of a team meeting around a whiteboard"></div>
  <div style="left:140px;top:153px;width:98px"><div class="hd">Header</div><p class="small">Lorem ipsum dolor sit amet, consectetur adipiscing elit. Vestibulum lacinia eros eu pharetra mollis.</p></div>
  <div class="photo" style="left:248px;top:152px;width:98px;height:66px" role="img" aria-label="Photo of a team meeting around a whiteboard"></div>
  <div style="left:355px;top:153px;width:98px"><div class="hd">Heading</div><p class="small">Lorem ipsum dolor sit amet, consectetur adipiscing elit. Vestibulum lacinia eros eu pharetra mollis.</p></div>
  <div class="note">Footnote here<br>Source here</div>
  <div class="rule"></div><div class="dots"></div><div class="brand">HARROWFIELD ENGINES</div>
  <div class="meta">Date | 09-06-2021 Page | 12</div>
</section>

<section class="slide c3 r4">
  <h2 class="title" style="top:20px;width:175px;font-size:13.5px;line-height:1.3">Lorem ipsum dolor sit amet, consectetur</h2>
  <div class="sub" style="top:63px">Sub title</div>
  <p class="small" style="left:33px;width:157px;top:84px;text-align:justify">Lorem ipsum dolor sit amet, consectetur adipiscing elit. Vestibulum lacinia eros eu pharetra mollis. Nullam vulputate purus mi, sed maximus est sodales mollis. Mauris nec vulputate eros. Cras lectus lacus, lacinia eu dapibus ac, tincidunt eu nisi. Suspendisse in volutpat risus. Nunc pharetra porttitor lorem. Vivamus at lectus sit amet lacus dictum tincidunt at vel magna. Donec blandit nulla ac erat condimentum, fringilla feugiat ex porttitor. Proin est odio, suscipit vitae magna at, bibendum tincidunt mi. Aenean facilisis pharetra lacus sed tempus. Nam finibus eu diam eu consectetur. Donec blandit nulla ac erat condimentum, fringilla feugiat ex porttitor. Proin est odio, suscipit vitae magna at, bibendum tincidunt mi. Aenean facilisis pharetra lacus sed tempus. Nam finibus eu diam eu consectetur.</p>
  <div class="hd" style="left:207px;top:50px">Header</div>
  <div class="photo" style="left:207px;top:64px;width:245px;height:159px" role="img" aria-label="Photo of a team meeting around a whiteboard"></div>
  <div class="note">Footnote here<br>Source here</div>
  <div class="rule"></div><div class="dots"></div><div class="brand">HARROWFIELD ENGINES</div>
  <div class="meta">Date | 09-06-2021 Page | 13</div>
</section>

<!-- Row 5 -->
<section class="slide c1 r5">
  <h2 class="title" style="top:92px;width:165px;font-size:13.5px;line-height:1.3">Lorem ipsum dolor sit amet, consectetur</h2>
  <p class="small" style="left:33px;width:160px;top:142px">Lorem ipsum dolor sit amet, consectetur adipiscing elit. Vestibulum lacinia eros eu pharetra mollis. Nullam vulputate purus mi, sed maximus est sodales mollis. Mauris nec vulputate eros.</p>
  <div class="photo" style="left:206px;top:42px;width:246px;height:187px" role="img" aria-label="Photo of a team meeting around a whiteboard"></div>
  <div class="note">Footnote here<br>Source here</div>
  <div class="rule"></div><div class="dots"></div><div class="brand">HARROWFIELD ENGINES</div>
  <div class="meta">Date | 09-06-2021 Page | 14</div>
</section>

<section class="slide c2 r5">
  <h2 class="title">Slide title</h2>
  <div class="tech" style="left:33px;top:51px;width:419px;height:191px" role="img" aria-label="Image of a hand reaching toward a glowing digital network"></div>
  <p class="small" style="left:53px;top:128px;width:122px;color:#fff">Lorem ipsum dolor sit amet, consectetur adipiscing elit. Vestibulum lacinia eros eu pharetra mollis. Nullam vulputate purus mi, sed maximus est sodales mollis. Mauris nec vulputate eros.</p>
  <div class="rule"></div><div class="dots"></div><div class="brand">HARROWFIELD ENGINES</div>
  <div class="meta">Date | 09-06-2021 Page | 15</div>
</section>

<section class="slide c3 r5">
  <h2 class="title">Slide title</h2><div class="sub">Sub title</div>
  <table class="grid" style="left:33px;top:79px;width:419px">
    <tr><th>Text</th><th>Text</th><th>Text</th><th>Text</th><th>Text</th></tr>
    <tr><td>Text</td><td>Text</td><td>Text</td><td>Text</td><td>Text</td></tr>
    <tr><td>Text</td><td>Text</td><td>Text</td><td>Text</td><td>Text</td></tr>
    <tr><td>Text</td><td>Text</td><td>Text</td><td>Text</td><td>Text</td></tr>
    <tr><td>Text</td><td>Text</td><td>Text</td><td>Text</td><td>Text</td></tr>
    <tr><td>Text</td><td>Text</td><td>Text</td><td>Text</td><td>Text</td></tr>
    <tr><td>Text</td><td>Text</td><td>Text</td><td>Text</td><td>Text</td></tr>
    <tr><td>Text</td><td>Text</td><td>Text</td><td>Text</td><td>Text</td></tr>
    <tr><td>Text</td><td>Text</td><td>Text</td><td>Text</td><td>Text</td></tr>
  </table>
  <div class="note">Footnote here<br>Source here</div>
  <div class="rule"></div><div class="dots"></div><div class="brand">HARROWFIELD ENGINES</div>
  <div class="meta">Date | 09-06-2021 Page | 16</div>
</section>

<!-- Row 6 -->
<section class="slide c1 r6">
  <h2 class="title">Slide title</h2><div class="sub">Subtitle</div>
  <div class="bar-head" style="left:33px;top:90px;width:94px">Heading</div>
  <div class="bar-head" style="left:141px;top:90px;width:94px">Heading</div>
  <div class="bar-head" style="left:249px;top:90px;width:94px">Heading</div>
  <div class="bar-head" style="left:357px;top:90px;width:95px">Heading</div>
  <ul class="list tiny small" style="left:35px;top:108px;width:90px"><li>Lorem ipsum dolor sit amet, consectetur adipiscing elit. Vestibulum lacinia eros eu pharetra mollis.</li><li>Nullam vulputate purus mi, sed maximus est sodales mollis. Mauris nec vulputate eros.</li><li>Cras lectus lacus, lacinia eu dapibus ac, tincidunt eu nisi. Suspendisse in volutpat risus.</li></ul>
  <ul class="list tiny small" style="left:143px;top:108px;width:90px"><li>Lorem ipsum dolor sit amet, consectetur adipiscing elit. Vestibulum lacinia eros eu pharetra mollis.</li><li>Nullam vulputate purus mi, sed maximus est sodales mollis. Mauris nec vulputate eros.</li><li>Cras lectus lacus, lacinia eu dapibus ac, tincidunt eu nisi. Suspendisse in volutpat risus.</li></ul>
  <ul class="list tiny small" style="left:251px;top:108px;width:90px"><li>Lorem ipsum dolor sit amet, consectetur adipiscing elit. Vestibulum lacinia eros eu pharetra mollis.</li><li>Nullam vulputate purus mi, sed maximus est sodales mollis. Mauris nec vulputate eros.</li><li>Cras lectus lacus, lacinia eu dapibus ac, tincidunt eu nisi. Suspendisse in volutpat risus.</li></ul>
  <ul class="list tiny small" style="left:359px;top:108px;width:90px"><li>Lorem ipsum dolor sit amet, consectetur adipiscing elit. Vestibulum lacinia eros eu pharetra mollis.</li><li>Nullam vulputate purus mi, sed maximus est sodales mollis. Mauris nec vulputate eros.</li><li>Cras lectus lacus, lacinia eu dapibus ac, tincidunt eu nisi. Suspendisse in volutpat risus.</li></ul>
  <div class="note">Footnote here<br>Source</div>
  <div class="rule"></div><div class="dots"></div><div class="brand">HARROWFIELD ENGINES</div>
  <div class="meta">Date | 09-06-2021 Page | 17</div>
</section>

<section class="slide c2 r6">
  <h2 class="title">Slide title</h2><div class="sub">Subtitle</div>
  <div class="underhead" style="left:33px;top:76px;width:96px">Heading</div>
  <div class="underhead" style="left:141px;top:76px;width:96px">Heading</div>
  <div class="underhead" style="left:249px;top:76px;width:96px">Heading</div>
  <div class="underhead" style="left:357px;top:76px;width:95px">Heading</div>
  <ul class="list tiny small" style="left:33px;top:92px;width:96px"><li>Lorem ipsum dolor sit amet, consectetur adipiscing elit. Vestibulum lacinia eros eu pharetra mollis.</li><li>Nullam vulputate purus mi, sed maximus est sodales mollis. Mauris nec vulputate eros.</li><li>Cras lectus lacus, lacinia eu dapibus ac, tincidunt eu nisi. Suspendisse in volutpat risus.</li></ul>
  <ul class="list tiny small" style="left:141px;top:92px;width:96px"><li>Lorem ipsum dolor sit amet, consectetur adipiscing elit. Vestibulum lacinia eros eu pharetra mollis.</li><li>Nullam vulputate purus mi, sed maximus est sodales mollis. Mauris nec vulputate eros.</li><li>Cras lectus lacus, lacinia eu dapibus ac, tincidunt eu nisi. Suspendisse in volutpat risus.</li></ul>
  <ul class="list tiny small" style="left:249px;top:92px;width:96px"><li>Lorem ipsum dolor sit amet, consectetur adipiscing elit. Vestibulum lacinia eros eu pharetra mollis.</li><li>Nullam vulputate purus mi, sed maximus est sodales mollis. Mauris nec vulputate eros.</li><li>Cras lectus lacus, lacinia eu dapibus ac, tincidunt eu nisi. Suspendisse in volutpat risus.</li></ul>
  <ul class="list tiny small" style="left:357px;top:92px;width:95px"><li>Lorem ipsum dolor sit amet, consectetur adipiscing elit. Vestibulum lacinia eros eu pharetra mollis.</li><li>Nullam vulputate purus mi, sed maximus est sodales mollis. Mauris nec vulputate eros.</li><li>Cras lectus lacus, lacinia eu dapibus ac, tincidunt eu nisi. Suspendisse in volutpat risus.</li></ul>
  <div class="band" style="left:33px;top:177px;width:419px">Lorem ipsum dolor sit amet, consectetur adipiscing elit. Vestibulum lacinia eros eu pharetra mollis</div>
  <div class="note">Footnote here<br>Source</div>
  <div class="rule"></div><div class="dots"></div><div class="brand">HARROWFIELD ENGINES</div>
  <div class="meta">Date | 09-06-2021 Page | 18</div>
</section>

<section class="slide c3 r6">
  <h2 class="title">Biography slide</h2><div class="sub">Team members</div>
  <div class="placeholder" style="left:33px;top:69px;width:70px;height:70px" role="img" aria-label="Team member portrait placeholder"></div>
  <div class="placeholder" style="left:120px;top:69px;width:70px;height:70px" role="img" aria-label="Team member portrait placeholder"></div>
  <div class="placeholder" style="left:207px;top:69px;width:70px;height:70px" role="img" aria-label="Team member portrait placeholder"></div>
  <div class="placeholder" style="left:294px;top:69px;width:70px;height:70px" role="img" aria-label="Team member portrait placeholder"></div>
  <div class="placeholder" style="left:382px;top:69px;width:70px;height:70px" role="img" aria-label="Team member portrait placeholder"></div>
  <div style="left:33px;top:144px;width:70px"><div class="hd">Name<br>Designation</div><p class="small" style="margin-top:4px">Lorem ipsum dolor sit amet, consectetur adipiscing elit. Vestibulum lacinia eros eu pharetra mollis. Nullam vulputate purus mi, sed</p></div>
  <div style="left:120px;top:144px;width:70px"><div class="hd">Name<br>Designation</div><p class="small" style="margin-top:4px">Lorem ipsum dolor sit amet, consectetur adipiscing elit. Vestibulum lacinia eros eu pharetra mollis. Nullam vulputate purus mi, sed</p></div>
  <div style="left:207px;top:144px;width:70px"><div class="hd">Name<br>Designation</div><p class="small" style="margin-top:4px">Lorem ipsum dolor sit amet, consectetur adipiscing elit. Vestibulum lacinia eros eu pharetra mollis. Nullam vulputate purus mi, sed</p></div>
  <div style="left:294px;top:144px;width:70px"><div class="hd">Name<br>Designation</div><p class="small" style="margin-top:4px">Lorem ipsum dolor sit amet, consectetur adipiscing elit. Vestibulum lacinia eros eu pharetra mollis. Nullam vulputate purus mi, sed</p></div>
  <div style="left:382px;top:144px;width:70px"><div class="hd">Name<br>Designation</div><p class="small" style="margin-top:4px">Lorem ipsum dolor sit amet, consectetur adipiscing elit. Vestibulum lacinia eros eu pharetra mollis. Nullam vulputate purus mi, sed</p></div>
  <div class="note">Footnote here<br>Source</div>
  <div class="rule"></div><div class="dots"></div><div class="brand">HARROWFIELD ENGINES</div>
  <div class="meta">Date | 09-06-2021 Page | 19</div>
</section>

<!-- Row 7 -->
<section class="slide c1 r7">
  <h2 class="title">Biography slide</h2><div class="sub">Team members</div>
  <div class="placeholder" style="left:33px;top:71px;width:20px;height:20px" role="img" aria-label="Portrait placeholder"></div>
  <div style="left:62px;top:71px;width:90px"><div class="small">Name<br>Designation</div><p class="small" style="font-size:3.6px">Lorem ipsum dolor sit amet, consectetur adipiscing elit. Vestibulum lacinia eros eu pharetra mollis. Nullam vulputate purus mi, sed</p></div>
  <div class="placeholder" style="left:183px;top:71px;width:20px;height:20px" role="img" aria-label="Portrait placeholder"></div>
  <div style="left:212px;top:71px;width:90px"><div class="small">Name<br>Designation</div><p class="small" style="font-size:3.6px">Lorem ipsum dolor sit amet, consectetur adipiscing elit. Vestibulum lacinia eros eu pharetra mollis. Nullam vulputate purus mi, sed</p></div>
  <div class="placeholder" style="left:333px;top:71px;width:20px;height:20px" role="img" aria-label="Portrait placeholder"></div>
  <div style="left:362px;top:71px;width:90px"><div class="small">Name<br>Designation</div><p class="small" style="font-size:3.6px">Lorem ipsum dolor sit amet, consectetur adipiscing elit. Vestibulum lacinia eros eu pharetra mollis. Nullam vulputate purus mi, sed</p></div>
  <div class="placeholder" style="left:33px;top:123px;width:20px;height:20px" role="img" aria-label="Portrait placeholder"></div>
  <div style="left:62px;top:123px;width:90px"><div class="small">Name<br>Designation</div><p class="small" style="font-size:3.6px">Lorem ipsum dolor sit amet, consectetur adipiscing elit. Vestibulum lacinia eros eu pharetra mollis. Nullam vulputate purus mi, sed</p></div>
  <div class="placeholder" style="left:183px;top:123px;width:20px;height:20px" role="img" aria-label="Portrait placeholder"></div>
  <div style="left:212px;top:123px;width:90px"><div class="small">Name<br>Designation</div><p class="small" style="font-size:3.6px">Lorem ipsum dolor sit amet, consectetur adipiscing elit. Vestibulum lacinia eros eu pharetra mollis. Nullam vulputate purus mi, sed</p></div>
  <div class="placeholder" style="left:333px;top:123px;width:20px;height:20px" role="img" aria-label="Portrait placeholder"></div>
  <div style="left:362px;top:123px;width:90px"><div class="small">Name<br>Designation</div><p class="small" style="font-size:3.6px">Lorem ipsum dolor sit amet, consectetur adipiscing elit. Vestibulum lacinia eros eu pharetra mollis. Nullam vulputate purus mi, sed</p></div>
  <div class="placeholder" style="left:33px;top:175px;width:20px;height:20px" role="img" aria-label="Portrait placeholder"></div>
  <div style="left:62px;top:175px;width:90px"><div class="small">Name<br>Designation</div><p class="small" style="font-size:3.6px">Lorem ipsum dolor sit amet, consectetur adipiscing elit. Vestibulum lacinia eros eu pharetra mollis. Nullam vulputate purus mi, sed</p></div>
  <div class="placeholder" style="left:183px;top:175px;width:20px;height:20px" role="img" aria-label="Portrait placeholder"></div>
  <div style="left:212px;top:175px;width:90px"><div class="small">Name<br>Designation</div><p class="small" style="font-size:3.6px">Lorem ipsum dolor sit amet, consectetur adipiscing elit. Vestibulum lacinia eros eu pharetra mollis. Nullam vulputate purus mi, sed</p></div>
  <div class="placeholder" style="left:333px;top:175px;width:20px;height:20px" role="img" aria-label="Portrait placeholder"></div>
  <div style="left:362px;top:175px;width:90px"><div class="small">Name<br>Designation</div><p class="small" style="font-size:3.6px">Lorem ipsum dolor sit amet, consectetur adipiscing elit. Vestibulum lacinia eros eu pharetra mollis. Nullam vulputate purus mi, sed</p></div>
  <div class="note">Footnote here<br>Source</div>
  <div class="rule"></div><div class="dots"></div><div class="brand">HARROWFIELD ENGINES</div>
  <div class="meta">Date | 09-06-2021 Page | 20</div>
</section>

<section class="slide c2 r7">
  <h2 class="title" style="font-size:13.5px">Team member name</h2><div class="sub">Designation</div>
  <div class="placeholder" style="left:33px;top:57px;width:165px;height:166px" role="img" aria-label="Team member portrait placeholder"></div>
  <p class="small" style="left:205px;top:70px;width:247px">Lorem ipsum dolor sit amet, consectetur adipiscing elit. Vestibulum lacinia eros eu pharetra mollis. Nullam vulputate purus mi, sed maximus est sodales mollis. Mauris nec vulputate eros. Cras lectus lacus, lacinia eu dapibus ac, tincidunt eu nisi. Suspendisse in volutpat risus.</p>
  <p class="small" style="left:205px;top:123px;width:247px">Lorem ipsum dolor sit amet, consectetur adipiscing elit. Vestibulum lacinia eros eu pharetra mollis. Nullam vulputate purus mi, sed maximus est sodales mollis. Mauris nec vulputate eros. Cras lectus lacus, lacinia eu dapibus ac, tincidunt eu nisi. Suspendisse in volutpat risus.</p>
  <p class="small" style="left:205px;top:176px;width:247px">Lorem ipsum dolor sit amet, consectetur adipiscing elit. Vestibulum lacinia eros eu pharetra mollis. Nullam vulputate purus mi, sed maximus est sodales mollis. Mauris nec vulputate eros. Cras lectus lacus, lacinia eu dapibus ac, tincidunt eu nisi. Suspendisse in volutpat risus.</p>
  <div class="note">Footnote here<br>Source</div>
  <div class="rule"></div><div class="dots"></div><div class="brand">HARROWFIELD ENGINES</div>
  <div class="meta">Date | 09-06-2021 Page | 21</div>
</section>

<section class="slide c3 r7">
  <div style="left:33px;top:0;width:178px;height:248px;background:linear-gradient(180deg,#eceef0 0%,#d4d8dc 55%,#9aa3ad 100%)" role="img" aria-label="Portrait photo of a team member holding a laptop"></div>
  <div style="left:242px;top:38px;font-size:8.5px;font-weight:700;color:var(--ink)">Name</div>
  <div style="left:242px;top:50px;font-size:8.5px;color:var(--ink)">Designation</div>
  <p class="small" style="left:242px;top:77px;width:210px">Lorem ipsum dolor sit amet, consectetur adipiscing elit. Vestibulum lacinia eros eu pharetra mollis. Nullam vulputate purus mi, sed maximus est sodales mollis. Mauris nec vulputate eros. Cras lectus lacus, lacinia eu dapibus ac, tincidunt eu nisi. Suspendisse in volutpat risus.</p>
  <p class="small" style="left:242px;top:127px;width:210px">Lorem ipsum dolor sit amet, consectetur adipiscing elit. Vestibulum lacinia eros eu pharetra mollis. Nullam vulputate purus mi, sed maximus est sodales mollis. Mauris nec vulputate eros. Cras lectus lacus, lacinia eu dapibus ac, tincidunt eu nisi. Suspendisse in volutpat risus.</p>
  <p class="small" style="left:242px;top:177px;width:210px">Lorem ipsum dolor sit amet, consectetur adipiscing elit. Vestibulum lacinia eros eu pharetra mollis. Nullam vulputate purus mi, sed maximus est sodales mollis. Mauris nec vulputate eros. Cras lectus lacus, lacinia eu dapibus ac, tincidunt eu nisi. Suspendisse in volutpat risus.</p>
  <div class="rule"></div><div class="dots"></div><div class="brand">HARROWFIELD ENGINES</div>
  <div class="meta">Date | 09-06-2021 Page | 22</div>
</section>

</body>
</html>
```